Cool modern, tech Business card design

Looking for a new business card design for our Managed IT Services company. We would like 2 sides, with the logo one one side horizontally and then the information on the back in either vertical or horizontal. We want our colors from the logo incorporated but also would like to see the color gray in there as well.

Target Market(s)

IT, Information Technology, Tech, Service

Industry/Entity Type

It Service

Contact Information for Business Card

Pavel Lind
Managing Partner
(P)742-318-6650 ext xxx
(F)742-318-6651
www.qelvantrixo.com

Font styles to use
Sans Serif

Colors
959595
000000
ec1f27

Requirements
Must have
• Logo on one side with some nice design or pattern
• Information on back in either vertical or horizontal format
Nice to have
• For it to look cool, tech, modern, stand out.

```html
<!DOCTYPE html>
<html lang="en">
<head>
<meta charset="utf-8">
<title>Qelvantrixo Business Card</title>
<link href="https://fonts.googleapis.com/css2?family=Arimo:wght@400;700&display=swap" rel="stylesheet">
<style>
  :root {
    --red: #ec1f27;
    --black: #000000;
    --ink: #1a1a1a;
    --gray: #959595;
    --gray-soft: #e6e6e6;
    --paper: #ffffff;
    --backdrop: #2b2b2b;
  }
  * { margin: 0; padding: 0; box-sizing: border-box; }
  html, body {
    width: 1200px; height: 900px; overflow: hidden;
    background: var(--backdrop);
    font-family: "Arimo", Arial, sans-serif;
  }
  .sheet {
    width: 1200px; height: 900px;
    display: flex; flex-direction: column; align-items: center; justify-content: center;
    gap: 24px;
  }
  .card {
    position: relative;
    width: 700px; height: 400px;
    background: var(--paper);
    border-radius: 24px;
    overflow: hidden;
  }

  /* Info side */
  .card-info .backdrop-shape {
    position: absolute; left: 250px; top: -40px;
    width: 300px; height: 360px;
    border-radius: 120px;
    background: radial-gradient(ellipse at center, #ececec 0%, #f4f4f4 55%, rgba(255,255,255,0) 75%);
  }
  .card-info .brand {
    position: absolute; left: 60px; top: 175px;
    display: flex; align-items: center; gap: 12px;
  }
  .brand-name {
    font-weight: 700; font-size: 40px; color: var(--ink); letter-spacing: -0.5px;
  }
  .brand-dot {
    width: 18px; height: 18px; background: var(--red); border-radius: 4px;
  }
  .card-info .divider {
    position: absolute; left: 378px; top: 95px; width: 1px; height: 100px; background: var(--gray);
  }
  .contact {
    position: absolute; left: 398px; top: 90px;
  }
  .person-name { font-size: 22px; font-weight: 700; color: var(--black); }
  .person-name .first { color: var(--red); }
  .person-title { font-size: 14px; color: var(--gray); margin-top: 2px; }
  .contact-list { list-style: none; margin-top: 12px; }
  .contact-list li {
    display: flex; align-items: center; gap: 10px;
    font-size: 14px; color: var(--ink); margin-bottom: 6px;
  }
  .icon {
    width: 18px; height: 18px; background: var(--red); border-radius: 4px;
    display: flex; align-items: center; justify-content: center;
  }
  .card-info .rule-top {
    position: absolute; left: 200px; top: 300px; width: 320px; height: 1px; background: var(--ink);
  }
  .card-info .web {
    position: absolute; right: 40px; top: 289px; font-size: 15px; font-weight: 700; color: var(--ink);
  }
  .web .accent { color: var(--red); }
  .card-info .corner-mark {
    position: absolute; left: 0; bottom: 0; width: 200px; height: 80px;
  }

  /* Logo side */
  .card-logo .pattern {
    position: absolute; inset: 0;
    background: linear-gradient(135deg, #f3f3f3 0%, #fafafa 50%, #f1f1f1 100%);
  }
  .card-logo .brand {
    position: absolute; left: 0; right: 0; top: 160px;
    display: flex; align-items: center; justify-content: center; gap: 14px;
  }
  .card-logo .brand-name { font-size: 52px; }
  .card-logo .brand-dot { width: 22px; height: 22px; }
  .card-logo .web {
    position: absolute; left: 0; right: 0; top: 280px; text-align: center;
    font-size: 16px; font-weight: 700; color: var(--ink);
  }
</style>
</head>
<body>
<main class="sheet">

  <section class="card card-info" aria-label="Contact side">
    <div class="backdrop-shape" role="img" aria-label="Faint gray brand decoration"></div>
    <div class="brand">
      <span class="brand-name">qelvantrixo</span>
      <span class="brand-dot"></span>
    </div>
    <div class="divider"></div>
    <div class="contact">
      <p class="person-name"><span class="first">Pavel</span> Lind</p>
      <p class="person-title">Managing Partner</p>
      <ul class="contact-list">
        <li>
          <span class="icon"><svg width="11" height="11" viewBox="0 0 24 24"><path fill="#fff" d="M6.6 10.8a15 15 0 0 0 6.6 6.6l2.2-2.2c.3-.3.7-.4 1-.2 1.1.4 2.3.6 3.6.6.6 0 1 .4 1 1V20c0 .6-.4 1-1 1A17 17 0 0 1 3 4c0-.6.4-1 1-1h3.5c.6 0 1 .4 1 1 0 1.3.2 2.5.6 3.6.1.3 0 .7-.2 1z"/></svg></span>
          742-318-6650 ext xxx
        </li>
        <li>
          <span class="icon"><svg width="11" height="11" viewBox="0 0 24 24"><path fill="#fff" d="M6 3h9l3 3v4H6zM4 11h16a2 2 0 0 1 2 2v6H2v-6a2 2 0 0 1 2-2zm2 5v2h12v-2z"/></svg></span>
          742-318-6651
        </li>
        <li>
          <span class="icon"><svg width="11" height="11" viewBox="0 0 24 24"><path fill="#fff" d="M2 5h20v14H2zm2 2v.5l8 5 8-5V7l-8 5z"/></svg></span>
          pavel@qelvantrixo.com
        </li>
      </ul>
    </div>
    <div class="rule-top"></div>
    <p class="web">www.<span class="accent">qelvantrixo</span>.com</p>
    <svg class="corner-mark" viewBox="0 0 200 80" aria-hidden="true">
      <line x1="0" y1="62" x2="70" y2="62" stroke="#1a1a1a" stroke-width="1"/>
      <line x1="70" y1="62" x2="90" y2="42" stroke="#1a1a1a" stroke-width="1"/>
      <line x1="108" y1="30" x2="200" y2="30" stroke="#1a1a1a" stroke-width="1"/>
      <rect x="88" y="22" width="18" height="18" rx="4" fill="#ec1f27"/>
    </svg>
  </section>

  <section class="card card-logo" aria-label="Logo side">
    <div class="pattern" role="img" aria-label="Soft gray repeating brand pattern"></div>
    <div class="brand">
      <span class="brand-name">qelvantrixo</span>
      <span class="brand-dot"></span>
    </div>
    <p class="web">www.<span class="accent">qelvantrixo</span>.com</p>
  </section>

</main>
</body>
</html>
```